Convert Adobe illustrator file to tri fold brochure

I have a line card that I need converted to a tri-fold brochure. I will fill in content details myself. I have uploaded the line card, please let me know if you have any questions.

```html
<!DOCTYPE html>
<html lang="en">
<head>
<meta charset="utf-8">
<title>Brightwave Systems – Tri-fold Brochure</title>
<link rel="stylesheet" href="https://fonts.googleapis.com/css2?family=Lato:wght@300;400;700&family=Cabin:wght@400;500&display=swap">
<style>
:root{
  --orange:#f0631c;
  --orange-light:#f7a12a;
  --orange-deep:#e2501a;
  --ink:#3a3a3a;
  --tail:#2e2e2e;
  --body:#4a4a4a;
  --paper:#ffffff;
  --band-dark:#3b3b3b;
}
*{box-sizing:border-box;margin:0;padding:0}
html,body{width:930px;height:1200px;overflow:hidden;background:var(--paper)}
body{position:relative;font-family:"Lato",sans-serif;color:var(--body)}

.sheet{position:absolute;left:29px;width:872px;height:566px;border:1px solid #555;overflow:hidden}
.sheet-outside{top:29px;background:linear-gradient(90deg,#fff 33.3%,#f1f1f1 33.3%,#fff 50%,#f1f1f1 66.6%,#fff 76%)}
.sheet-inside{top:605px;background:linear-gradient(180deg,#fdfdfd 0%,#efefef 55%,#d9d9d9 100%)}
.fold{position:absolute;top:0;bottom:0;width:1px;background:rgba(0,0,0,.06)}

/* cover */
.cover{position:absolute;left:0;top:0;width:291px;height:566px}
.cover svg{position:absolute;inset:0}
.cover-headline{position:absolute;left:0;width:291px;top:386px;text-align:center;font-family:"Cabin",sans-serif;font-weight:400;font-size:29px;line-height:42px;color:#fff;letter-spacing:-.5px;text-shadow:0 2px 3px rgba(0,0,0,.45)}
.cover-badge{position:absolute;left:37px;top:470px;width:221px;height:68px;background:#fff;border-radius:6px;box-shadow:0 1px 4px rgba(0,0,0,.3);text-align:center;padding-top:6px}
.cover-photo{display:block;width:132px;height:26px;margin:3px auto 0;border-radius:13px;background:linear-gradient(90deg,#9b1b1b,#c0281f 30%,#f39a2a 45%,#a3201c 60%,#b8261d)}
.cover-tagline{font-family:"Cabin",sans-serif;font-size:9px;color:#222;margin-top:1px}
.cover-url{position:absolute;left:0;bottom:0;width:291px;height:22px;background:var(--band-dark);color:#fff;font-size:12.5px;line-height:22px;text-align:center}

/* brand lockup */
.brand{display:inline-flex;align-items:center;gap:6px}
.brand-mark{width:14px;height:14px;background:var(--orange)}
.brand-name{font-family:"Lato",sans-serif;font-weight:700;color:var(--ink);letter-spacing:.5px;text-transform:uppercase;white-space:nowrap}
.brand-small .brand-name{font-size:13px}
.brand-large{position:absolute;flex-direction:column;align-items:flex-start;gap:3px}
.brand-large .brand-row{display:flex;align-items:center;gap:9px}
.brand-large .brand-mark{width:30px;height:30px}
.brand-large .brand-name{font-size:20px;line-height:22px;white-space:normal;width:150px}
.brand-motto{font-size:6px;color:var(--ink);letter-spacing:.3px;margin-left:39px;text-transform:uppercase}

/* section tabs */
.tab{position:absolute;height:30px}
.tab-bar{position:absolute;inset:0;background:linear-gradient(180deg,var(--orange) 0%,var(--orange-deep) 100%);clip-path:polygon(0 0,100% 0,calc(100% - 16px) 100%,0 100%);color:#fff;font-weight:300;font-size:17px;line-height:30px;padding-left:14px;display:flex;align-items:center;gap:10px}
.tab-tail{position:absolute;top:0;right:-16px;width:28px;height:100%;background:var(--tail);clip-path:polygon(16px 0,28px 0,12px 100%,0 100%)}
.tab-bar svg{flex:none}
.tab-tall{height:40px}
.tab-tall .tab-bar{font-size:15.5px;line-height:19px}
.tab-label-wrap{width:150px}
.tab-short .tab-bar{padding-left:8px;font-size:17px}

.copy{position:absolute;font-size:8.4px;line-height:13.4px;color:var(--body)}
.copy p{margin-bottom:7px}
.inside-band{position:absolute;right:0;bottom:0;width:291px;height:21px;background:var(--band-dark)}
</style>
</head>
<body>

<section class="sheet sheet-outside">
  <div class="fold" style="left:291px"></div>
  <div class="fold" style="left:582px"></div>

  <div class="cover">
    <svg width="291" height="566" viewBox="0 0 291 566" aria-hidden="true">
      <defs>
        <linearGradient id="coverTop" x1="0" y1="0" x2="1" y2="0">
          <stop offset="0" stop-color="#ee6b1e"/><stop offset="1" stop-color="#f9a62b"/>
        </linearGradient>
        <linearGradient id="coverBottom" x1="0" y1="0" x2="0" y2="1">
          <stop offset="0" stop-color="#f27a24"/><stop offset="1" stop-color="#e2501a"/>
        </linearGradient>
      </defs>
      <rect width="291" height="566" fill="#f4f4f4"/>
      <polygon points="0,0 291,0 291,40 0,115" fill="url(#coverTop)"/>
      <polygon points="0,115 291,40 291,44 0,119" fill="#ffffff"/>
      <polygon points="0,362 291,320 291,566 0,566" fill="url(#coverBottom)"/>
      <polygon points="0,362 291,320 291,336 0,378" fill="#3b3b3b"/>
    </svg>
    <div role="img" aria-label="Large faint brand emblem watermark" style="position:absolute;left:20px;top:110px;width:250px;height:230px;background:radial-gradient(ellipse at center,#e6e6e6 0%,#ececec 55%,rgba(244,244,244,0) 75%)"></div>
    <h1 class="cover-headline">Making technology<br>easy for you...</h1>
    <div class="cover-badge">
      <span class="brand brand-small"><span class="brand-mark"></span><span class="brand-name">Brightwave Systems</span></span>
      <span class="cover-photo" role="img" aria-label="Row of red apples with one orange among them"></span>
      <p class="cover-tagline">Bright ideas, delivered with real care!</p>
    </div>
    <div class="cover-url">www.brightwavesystems.net</div>
  </div>

  <!-- middle panel -->
  <div class="tab" style="left:291px;top:37px;width:112px">
    <div class="tab-bar">BYOD
      <svg width="22" height="20" viewBox="0 0 22 20" fill="none" stroke="#fff" stroke-width="1.6"><rect x="2" y="3" width="14" height="10"/><line x1="9" y1="13" x2="9" y2="17"/><line x1="5" y1="17" x2="13" y2="17"/><rect x="14" y="8" width="6" height="10" fill="#f0631c"/></svg>
    </div><div class="tab-tail"></div>
  </div>

  <div class="tab" style="left:291px;top:213px;width:212px">
    <div class="tab-bar">Technology Training
      <svg width="30" height="24" viewBox="0 0 30 24" fill="#fff"><circle cx="15" cy="4" r="3"/><rect x="11.5" y="8" width="7" height="9" rx="2"/><circle cx="6" cy="7" r="2.6"/><rect x="3" y="10.5" width="6" height="8" rx="2"/><circle cx="24" cy="7" r="2.6"/><rect x="21" y="10.5" width="6" height="8" rx="2"/><rect x="13" y="17" width="4" height="6"/></svg>
    </div><div class="tab-tail"></div>
  </div>
  <div class="copy" style="left:308px;top:252px;width:266px">
    <p>The pace of technology never has people in mind. We all want to make use of the latest abilities, but who has the time to learn it all?</p>
    <p>Keeping up is our job and we help you by making sure you only focus on the things you need. From online resources to in person training sessions, we first help you</p>
  </div>

  <div class="tab tab-tall" style="left:291px;top:378px;width:238px">
    <div class="tab-bar"><span class="tab-label-wrap">Backup and Disaster Recovery</span>
      <svg width="24" height="22" viewBox="0 0 24 22" fill="none" stroke="#fff" stroke-width="1.6"><rect x="2" y="2" width="20" height="14"/><line x1="12" y1="16" x2="12" y2="20"/><line x1="7" y1="20" x2="17" y2="20"/><path d="M8 12 L15 5 M14 12 L9 6"/></svg>
    </div><div class="tab-tail"></div>
  </div>
  <div class="copy" style="left:308px;top:426px;width:266px">
    <p>Are you still maintaining a backup and disaster recovery plan? Step up to a Business Continuity plan that keeps you going, all while cutting your costs.</p>
    <p>How does it work? We back up entire servers and virtualize them so they can run in the Cloud, keeping you from downtime. No redundant hardware to buy, just the smartest way to expect the unexpected.</p>
  </div>

  <!-- right panel -->
  <div class="tab" style="left:582px;top:37px;width:156px">
    <div class="tab-bar">Total Support
      <svg width="24" height="22" viewBox="0 0 24 22" fill="none" stroke="#fff" stroke-width="1.6"><rect x="6" y="2" width="12" height="9"/><line x1="12" y1="11" x2="12" y2="14"/><path d="M2 12 L6 17 H10 M22 12 L18 17 H14"/></svg>
    </div><div class="tab-tail"></div>
  </div>
  <div class="copy" style="left:592px;top:70px;width:268px">
    <p>Don't go it alone. We offer fast and reliable support, plus remote desktop management and maintenance for your workstations for one monthly fee. No more racking up bills whenever you need support.</p>
    <p>Our Steady Care desktop plan provides preventative maintenance services and bundled managed anti-virus.</p>
  </div>

  <div class="tab" style="left:582px;top:171px;width:198px">
    <div class="tab-bar">Cloud Computing
      <svg width="26" height="20" viewBox="0 0 26 20" fill="none" stroke="#fff" stroke-width="1.8"><path d="M7 16 H5 A4 4 0 0 1 6 8 A6 6 0 0 1 18 6 A5 5 0 0 1 20 16 H19"/><path d="M13 18 V10 M10 13 L13 10 L16 13"/></svg>
    </div><div class="tab-tail"></div>
  </div>
  <div class="copy" style="left:592px;top:210px;width:268px">
    <p>It is becoming increasingly expensive to host your own servers. Cloud solutions not only offer a lower total cost of ownership due to the economy of scale, but are more reliable. Imagine email that never goes down and can be accessed from anywhere on any device.</p>
    <p>Are you a non-profit or educational institution? There are programs available that provide these services at little to no cost, let Brightwave Systems help you take advantage today!</p>
  </div>

  <div class="tab" style="left:582px;top:328px;width:180px">
    <div class="tab-bar">Network Security
      <svg width="22" height="18" viewBox="0 0 22 18" fill="none" stroke="#fff" stroke-width="1.4"><rect x="1" y="1" width="20" height="16"/><path d="M1 6 H21 M1 11.5 H21 M8 1 V6 M15 1 V6 M5 6 V11.5 M12 6 V11.5 M18 6 V11.5 M8 11.5 V17 M15 11.5 V17"/></svg>
    </div><div class="tab-tail"></div>
  </div>
  <div class="copy" style="left:592px;top:366px;width:268px">
    <p>How Secure is your Network?<br>Are you at risk? It's time to get proactive.</p>
    <p>The Internet offers significant benefits to organizations of all sizes, but with it come many security issues. From Malware to Data Theft, layering protection into your IT is more important every day. We review your needs and find what works best for you.</p>
  </div>

  <div class="brand brand-large" style="left:622px;top:486px">
    <span class="brand-row"><span class="brand-mark"></span><span class="brand-name">Brightwave Systems</span></span>
    <span class="brand-motto">Smart support for every team</span>
  </div>
</section>

<section class="sheet sheet-inside">
  <div class="fold" style="left:291px"></div>
  <div class="fold" style="left:582px"></div>

  <div class="tab tab-short" style="left:0;top:38px;width:156px"><div class="tab-bar">Technology
    <svg width="24" height="22" viewBox="0 0 24 22" fill="none" stroke="#fff" stroke-width="1.6"><rect x="6" y="2" width="12" height="9"/><line x1="12" y1="11" x2="12" y2="14"/><path d="M2 12 L6 17 H10 M22 12 L18 17 H14"/></svg></div><div class="tab-tail"></div></div>
  <div class="tab tab-short" style="left:291px;top:38px;width:156px"><div class="tab-bar">Technology
    <svg width="24" height="22" viewBox="0 0 24 22" fill="none" stroke="#fff" stroke-width="1.6"><rect x="6" y="2" width="12" height="9"/><line x1="12" y1="11" x2="12" y2="14"/><path d="M2 12 L6 17 H10 M22 12 L18 17 H14"/></svg></div><div class="tab-tail"></div></div>
  <div class="tab tab-short" style="left:582px;top:38px;width:156px"><div class="tab-bar">Technology
    <svg width="24" height="22" viewBox="0 0 24 22" fill="none" stroke="#fff" stroke-width="1.6"><rect x="6" y="2" width="12" height="9"/><line x1="12" y1="11" x2="12" y2="14"/><path d="M2 12 L6 17 H10 M22 12 L18 17 H14"/></svg></div><div class="tab-tail"></div></div>

  <div class="tab tab-short" style="left:0;top:184px;width:156px"><div class="tab-bar">Technology
    <svg width="30" height="24" viewBox="0 0 30 24" fill="#fff"><circle cx="15" cy="4" r="3"/><rect x="11.5" y="8" width="7" height="9" rx="2"/><circle cx="6" cy="7" r="2.6"/><rect x="3" y="10.5" width="6" height="8" rx="2"/><circle cx="24" cy="7" r="2.6"/><rect x="21" y="10.5" width="6" height="8" rx="2"/><rect x="13" y="17" width="4" height="6"/></svg></div><div class="tab-tail"></div></div>
  <div class="tab tab-short" style="left:291px;top:184px;width:156px"><div class="tab-bar">Technology
    <svg width="30" height="24" viewBox="0 0 30 24" fill="#fff"><circle cx="15" cy="4" r="3"/><rect x="11.5" y="8" width="7" height="9" rx="2"/><circle cx="6" cy="7" r="2.6"/><rect x="3" y="10.5" width="6" height="8" rx="2"/><circle cx="24" cy="7" r="2.6"/><rect x="21" y="10.5" width="6" height="8" rx="2"/><rect x="13" y="17" width="4" height="6"/></svg></div><div class="tab-tail"></div></div>
  <div class="tab tab-short" style="left:582px;top:184px;width:156px"><div class="tab-bar">Technology
    <svg width="30" height="24" viewBox="0 0 30 24" fill="#fff"><circle cx="15" cy="4" r="3"/><rect x="11.5" y="8" width="7" height="9" rx="2"/><circle cx="6" cy="7" r="2.6"/><rect x="3" y="10.5" width="6" height="8" rx="2"/><circle cx="24" cy="7" r="2.6"/><rect x="21" y="10.5" width="6" height="8" rx="2"/><rect x="13" y="17" width="4" height="6"/></svg></div><div class="tab-tail"></div></div>

  <div class="tab tab-short" style="left:0;top:341px;width:156px"><div class="tab-bar">Technology
    <svg width="22" height="20" viewBox="0 0 22 20" fill="none" stroke="#fff" stroke-width="1.6"><rect x="2" y="3" width="14" height="10"/><line x1="9" y1="13" x2="9" y2="17"/><line x1="5" y1="17" x2="13" y2="17"/><rect x="14" y="8" width="6" height="10" fill="#f0631c"/></svg></div><div class="tab-tail"></div></div>
  <div class="tab tab-short" style="left:291px;top:341px;width:156px"><div class="tab-bar">Technology
    <svg width="22" height="20" viewBox="0 0 22 20" fill="none" stroke="#fff" stroke-width="1.6"><rect x="2" y="3" width="14" height="10"/><line x1="9" y1="13" x2="9" y2="17"/><line x1="5" y1="17" x2="13" y2="17"/><rect x="14" y="8" width="6" height="10" fill="#f0631c"/></svg></div><div class="tab-tail"></div></div>
  <div class="tab tab-short" style="left:582px;top:341px;width:156px"><div class="tab-bar">Technology
    <svg width="22" height="20" viewBox="0 0 22 20" fill="none" stroke="#fff" stroke-width="1.6"><rect x="2" y="3" width="14" height="10"/><line x1="9" y1="13" x2="9" y2="17"/><line x1="5" y1="17" x2="13" y2="17"/><rect x="14" y="8" width="6" height="10" fill="#f0631c"/></svg></div><div class="tab-tail"></div></div>

  <div class="brand brand-large" style="left:622px;top:468px">
    <span class="brand-row"><span class="brand-mark"></span><span class="brand-name">Brightwave Systems</span></span>
    <span class="brand-motto">Smart support for every team</span>
  </div>
  <div class="inside-band"></div>
</section>

</body>
</html>
```